Title loan company needs a postcard design, front/back, for marketing to former customers

We need a clean postcard design for the purpose of a mailer to engage former customers to come in and take out a loan.
We want to reinforce the benefits of doing business with us and give them an incentive offer to borrow money with us again.

The special offer: $50 Bonus Cash on your next loan

Some points or benefits we offer:
-No Credit Check
-Instant Approval
-Easy Payments
-15 Minute Loans
-Coin Steady Approved-I am providing this as a image for a state association we are members of. You may use the logo or use it as a benefit.
-Satisfaction Guarantee-I am providing this as an image as a guarantee. I personally feel that this should image should be used as a reinforcement of said guarantee.

The loan product is know as a title loan. The customer pledges the car title to their vehicle as security for the loan in exchange for cash.

Front and back of the card should have a call to action.
Looking for a clean design for the front and back of the postcard.
Back of the card should have a space for postage stamp, or indicia, and enough room for a mailing label

Visit our website for any additional information that you may have or ask me directly.

pinemarkfunding.com

Hex color codes of the logo should you incorporate this into the design.
Light Green in Logo: #b7dc78
Dark Green in Logo: #00953a
Yellow in Logo: #ffdd00

I am attaching our logo, the coin steady seal, and the guarantee shield.
I am also attaching templates for illustrator, photoshop, acrobat. Use one of the templates as it has the correct bleeds for my printer. If you need another template let me know.

Reason: I am extending the deadline but I only really need a day before i choose the final design. Had a technical error that prevents me from getting this done & it should be rectified by the end of the day today?

Target Market(s)

25-54
Male/Female = 50% Split

Industry/Entity Type

Loan

Font styles to use
Serif
Sans Serif

Requirements
Must have
• Clean Design, Call to Action, Draw attention to special offer
Nice to have
• Use of some of the colors in logo, hex color codes are in description, for branding purposes! Not a requirement! Let see what you bring to the table.

```html
<!DOCTYPE html>
<html lang="en">
<head>
<meta charset="utf-8">
<title>Pinemark Funding – Postcard Front and Back</title>
<link href="https://fonts.googleapis.com/css2?family=Oswald:wght@500;600&family=Lato:wght@400;700&display=swap" rel="stylesheet">
<style>
  :root{
    --green:#00953a;
    --green-light:#b7dc78;
    --yellow:#ffdd00;
    --charcoal:#333333;
    --ink:#222222;
    --red:#e3141f;
    --stamp:#c8c8c8;
    --paper:#ffffff;
  }
  *{box-sizing:border-box;margin:0;padding:0}
  html,body{width:1200px;height:1200px;overflow:hidden;background:var(--paper)}
  body{position:relative;font-family:"Lato",Arial,sans-serif;color:var(--ink)}
  .postcard{position:absolute;left:241px;width:748px;height:529px;background:var(--paper);overflow:hidden;box-shadow:0 3px 10px rgba(0,0,0,.25)}
  .postcard--front{top:56px}
  .postcard--back{top:616px}
  .postcard svg.shapes{position:absolute;inset:0;width:748px;height:529px}

  .brand{position:absolute;display:flex;align-items:center;gap:8px;white-space:nowrap}
  .brand__dot{border-radius:50%;background:var(--green);flex:none}
  .brand__name{font-family:"Lato",Arial,sans-serif;font-weight:700;color:var(--ink);line-height:1}
  .front .brand{left:20px;top:100px}
  .front .brand__dot{width:26px;height:26px}
  .front .brand__name{font-size:26px}

  .headline{position:absolute;left:19px;top:166px;font-family:"Oswald",sans-serif;line-height:1.05;white-space:nowrap}
  .headline__main{font-size:30px;font-weight:600;color:var(--green);display:block;letter-spacing:-.4px}
  .headline__sub{font-size:22px;font-weight:600;color:var(--charcoal);display:block;margin-top:2px}
  .intro{position:absolute;left:19px;top:254px;width:314px;font-size:12.4px;line-height:16.7px;text-align:justify;color:var(--ink)}

  .cta{position:absolute;color:#fff}
  .cta__line{font-family:"Oswald",sans-serif;font-weight:500;font-size:26px;line-height:1}
  .cta__label{color:var(--yellow)}
  .cta__web{font-size:16px;margin-top:4px}
  .front .cta{left:14px;top:470px}
  .back .cta{left:142px;top:470px;text-align:center}

  .offer{position:absolute;width:164px;height:164px;border-radius:50%;background:var(--yellow);padding:5px}
  .offer__ring{width:100%;height:100%;border-radius:50%;background:var(--green);padding:5px}
  .offer__face{width:100%;height:100%;border-radius:50%;background:#fff;display:flex;flex-direction:column;align-items:center;justify-content:center;font-family:"Oswald",sans-serif;line-height:1}
  .offer__top{display:flex;align-items:center;gap:2px}
  .offer__amount{color:var(--red);font-size:40px;font-weight:600}
  .offer__bonus{display:flex;flex-direction:column;font-size:16px;font-weight:500}
  .offer__bonus span:first-child{color:var(--green)}
  .offer__next{color:var(--green);font-size:26px;font-weight:500;margin-top:2px}
  .offer__loan{font-size:33px;font-weight:500;color:var(--ink);margin-top:2px}
  .front .offer{left:558px;top:338px}
  .back .offer{left:219px;top:218px}

  .seal{position:absolute}
  .seal--shield{width:58px;height:68px}
  .seal--round{width:70px;height:70px}

  .scene{position:absolute}
  .scene--gold{left:300px;top:0;width:448px;height:380px;clip-path:polygon(0 0,100% 0,100% 100%,23% 100%)}
  .scene--sprouts{left:0;top:0;width:342px;height:168px;background:linear-gradient(#9cc86a,#c7ae78 55%,#fff)}

  .back .brand{left:16px;top:170px}
  .back .brand__dot{width:22px;height:22px}
  .back .brand__name{font-size:23px}
  .benefits{position:absolute;left:25px;top:224px}
  .benefits__title{font-family:"Oswald",sans-serif;font-weight:500;font-size:21px;color:var(--green);margin-bottom:6px}
  .benefits__list{list-style:none}
  .benefits__item{display:flex;align-items:center;gap:7px;font-size:18px;height:30px}
  .benefits__tick{width:14px;height:14px}

  .stamp-box{position:absolute;left:646px;top:14px;width:85px;height:99px;background:var(--stamp)}
</style>
</head>
<body>

<section class="postcard postcard--front front">
  <svg class="shapes" viewBox="0 0 748 529" aria-hidden="true">
    <defs>
      <linearGradient id="goldScene" x1="0" y1="0" x2="1" y2="1">
        <stop offset="0" stop-color="#fbfaf6"/>
        <stop offset=".45" stop-color="#d9b565"/>
        <stop offset=".75" stop-color="#b98a34"/>
        <stop offset="1" stop-color="#f1ece2"/>
      </linearGradient>
    </defs>
    <polygon points="263,0 383,392 748,472 748,480 378,400 255,0" fill="var(--yellow)"/>
    <polygon points="283,0 300,0 402,378 748,440 748,456 391,386" fill="var(--green)"/>
    <polygon points="300,0 748,0 748,440 402,378" fill="url(#goldScene)"/>
    <polygon points="0,456 279,456 455,529 0,529" fill="var(--charcoal)"/>
    <polygon points="430,520 748,518 748,529 455,529" fill="var(--yellow)"/>
  </svg>
  <div class="scene scene--gold" role="img" aria-label="Photo of a gold house with a key surrounded by stacks of gold coins"></div>

  <div class="brand"><span class="brand__dot"></span><span class="brand__name">Pinemark Funding</span></div>

  <h1 class="headline">
    <span class="headline__main">GETTING CASH IS EASY</span>
    <span class="headline__sub">AT PINEMARK FUNDING</span>
  </h1>

  <p class="intro">Pinemark Funding knows that every customer has different needs. We promise that no one else will work as hard as we do to earn and keep your business. As a trusted lender since 1995, we pride ourselves on providing critical funds to hard-working people who may simply need a little help from time to time. Our friendly and qualified loan counselors take the time to understand your circumstances and will work hard to find loans that are right for your needs.</p>

  <svg class="seal seal--shield" style="left:396px;top:424px" viewBox="0 0 58 68" role="img" aria-label="Satisfaction guarantee shield">
    <path d="M29 2 L55 10 L53 40 Q48 58 29 66 Q10 58 5 40 L3 10 Z" fill="#6aa84f" stroke="#c9c9c9" stroke-width="3"/>
  </svg>
  <svg class="seal seal--round" style="left:469px;top:424px" viewBox="0 0 70 70" role="img" aria-label="Coin Steady Approved seal">
    <circle cx="35" cy="35" r="33" fill="#5d9b3a"/>
    <circle cx="35" cy="35" r="24" fill="#7bb655"/>
    <rect x="4" y="29" width="62" height="12" fill="#2f6b22"/>
  </svg>

  <div class="offer"><div class="offer__ring"><div class="offer__face">
    <div class="offer__top"><span class="offer__amount">$50</span><span class="offer__bonus"><span>Bonus</span><span>Cash on</span></span></div>
    <div class="offer__next">your next</div>
    <div class="offer__loan">LOAN</div>
  </div></div></div>

  <div class="cta">
    <div class="cta__line"><span class="cta__label">CALL:</span> 01987654320</div>
    <div class="cta__web">www.pinemarkfunding.com</div>
  </div>
</section>

<section class="postcard postcard--back back">
  <svg class="shapes" viewBox="0 0 748 529" aria-hidden="true">
    <polygon points="342,0 369,0 358,235 342,250" fill="var(--green)"/>
    <polygon points="375,0 391,0 368,230 360,236" fill="var(--yellow)"/>
    <polygon points="0,452 260,352 300,352 0,470" fill="var(--green)"/>
    <polygon points="0,478 300,360 340,360 0,497" fill="var(--yellow)"/>
    <polygon points="351,363 455,529 0,529 0,503" fill="var(--charcoal)"/>
  </svg>
  <div class="scene scene--sprouts" role="img" aria-label="Photo of green seedlings growing from stacks of coins"></div>

  <div class="stamp-box" aria-label="Postage stamp area"></div>

  <div class="brand"><span class="brand__dot"></span><span class="brand__name">Pinemark Funding</span></div>

  <div class="benefits">
    <h2 class="benefits__title">Benefits we offer</h2>
    <ul class="benefits__list">
      <li class="benefits__item"><svg class="benefits__tick" viewBox="0 0 14 14"><path d="M1 8 L5 12 L13 2" fill="none" stroke="var(--green)" stroke-width="2.6"/></svg>No Credit Check</li>
      <li class="benefits__item"><svg class="benefits__tick" viewBox="0 0 14 14"><path d="M1 8 L5 12 L13 2" fill="none" stroke="var(--green)" stroke-width="2.6"/></svg>Instant Approval</li>
      <li class="benefits__item"><svg class="benefits__tick" viewBox="0 0 14 14"><path d="M1 8 L5 12 L13 2" fill="none" stroke="var(--green)" stroke-width="2.6"/></svg>Easy Payments</li>
      <li class="benefits__item"><svg class="benefits__tick" viewBox="0 0 14 14"><path d="M1 8 L5 12 L13 2" fill="none" stroke="var(--green)" stroke-width="2.6"/></svg>15 Minute Loans</li>
    </ul>
  </div>

  <div class="offer"><div class="offer__ring"><div class="offer__face">
    <div class="offer__top"><span class="offer__amount">$50</span><span class="offer__bonus"><span>Bonus</span><span>Cash on</span></span></div>
    <div class="offer__next">your next</div>
    <div class="offer__loan">LOAN</div>
  </div></div></div>

  <svg class="seal seal--shield" style="left:225px;top:403px;width:52px;height:60px" viewBox="0 0 58 68" role="img" aria-label="Satisfaction guarantee shield">
    <path d="M29 2 L55 10 L53 40 Q48 58 29 66 Q10 58 5 40 L3 10 Z" fill="#6aa84f" stroke="#c9c9c9" stroke-width="3"/>
  </svg>
  <svg class="seal seal--round" style="left:293px;top:402px;width:62px;height:62px" viewBox="0 0 70 70" role="img" aria-label="Coin Steady Approved seal">
    <circle cx="35" cy="35" r="33" fill="#5d9b3a"/>
    <circle cx="35" cy="35" r="24" fill="#7bb655"/>
    <rect x="4" y="29" width="62" height="12" fill="#2f6b22"/>
  </svg>

  <div class="cta">
    <div class="cta__line"><span class="cta__label">CALL:</span> 01987654320</div>
    <div class="cta__web">www.pinemarkfunding.com</div>
  </div>
</section>

</body>
</html>
```